Award winning photographer needs a website.

I need a Plumleaf website that showcases my photos. I want them arranged via category, which might be a specific place or a theme. Here are categories I am thinking of:
1. Yarra Valley and Ranges
2. East coast Tasmania
3. Landscapes
4. Seascapes
5. Urban
6. Nepal
7. Macro
I need to be able to upload and download the photos myself. Currently, there is no need for this site to have an ecommerce component. I would like a blog page where I can post about my photographic adventures and maybe add some short videos of me on my way to the shoot, or of the people I meet. I also want to have it so that each photo has a title and if people click on a photo they can read a story about how I came to shoot it etc. There will also be my contact details and how to purchase a print which will happen through other communications. Like i mentioned, no e commerce at this point. I would like a page for awards as I have several. Here are some URLs of sites I like to give you some idea of what I'm looking at:

https://www.vendrimask.com/
https://tobyfarnellphotography.example/
https://www.maudelinskyphotography.example/

I can upload some images for you to start putting together someting if that hepls

Industry/Entity Type

Photography

Coding

Coded - Design and coding required

Number of Pages Required

5+ page

Font styles to use
Sans Serif

Requirements
Must have
• Multiple pages to display photos in different categories

```html
<!DOCTYPE html>
<html lang="en">
<head>
<meta charset="utf-8">
<title>Corwin Ashdale — Award Winning Photographer</title>
<link href="https://fonts.googleapis.com/css2?family=Cinzel:wght@400&family=Lato:ital,wght@0,300;0,400;0,700;1,300&family=Dancing+Script:wght@500&display=swap" rel="stylesheet">
<style>
:root{
  --ink:#222;
  --body:#333;
  --muted:#555;
  --white:#fff;
  --footer:#262626;
  --rule:#444;
  --card-line:#ececec;
}
*{box-sizing:border-box;margin:0;padding:0}
html,body{width:1200px;height:3557px;overflow:hidden}
body{position:relative;font-family:"Lato",sans-serif;color:var(--body);background:var(--white)}
a{color:inherit}
.abs{position:absolute}
.heading{font-family:"Cinzel",serif;font-weight:400;color:var(--ink);letter-spacing:1px}
.section-title{position:absolute;left:0;width:1200px;text-align:center;font-size:38px}

/* hero */
.hero{left:0;top:0;width:1200px;height:514px;
  background:linear-gradient(180deg,#3a3f6e 0%,#8a6a92 22%,#c78fa8 35%,#5b5f9a 52%,#3b4a80 62%,#3f6a3a 72%,#4f7a2c 85%,#3a5426 100%)}
.brand{left:112px;top:38px;font-family:"Lato",sans-serif;font-weight:300;font-size:30px;color:var(--white);letter-spacing:.5px}
.nav{right:110px;top:48px;display:flex;gap:30px;font-size:15px;color:var(--white)}
.hero-title{left:0;top:380px;width:1200px;text-align:center;font-size:41px;color:var(--white);text-shadow:0 2px 6px rgba(0,0,0,.35)}

/* welcome */
.welcome-photo{left:112px;top:587px;width:442px;height:382px;background:linear-gradient(170deg,#e0305c 0%,#c8284a 40%,#5a4a2a 70%,#b83a2c 100%)}
.welcome-text{left:613px;top:607px;width:480px}
.welcome-text h2{font-size:36px;margin-bottom:18px}
.welcome-text p{font-size:15px;line-height:28.5px;margin-bottom:9px}
.signature{font-family:"Dancing Script",cursive;font-size:30px;color:var(--ink);margin-top:18px}

/* collections */
.collections{left:112px;top:1149px;width:978px;display:grid;grid-template-columns:repeat(4,1fr);gap:11px 11px}
.tile{position:relative;height:178px}
.tile span{position:absolute;left:0;right:0;bottom:26px;text-align:center;color:var(--white);font-size:15px;text-shadow:0 1px 3px rgba(0,0,0,.5)}

/* gallery */
.gallery{left:112px;top:1675px;width:978px;display:grid;grid-template-columns:repeat(3,1fr);gap:15px 16px}
.shot{position:relative;height:262px}
.shot.feature{background:linear-gradient(180deg,#5a4a3a,#3c3830);color:var(--white);text-align:center;padding:40px 22px 0}
.shot.feature h3{font-weight:400;font-size:15px;margin-bottom:12px}
.shot.feature p{font-size:13px;line-height:24px}
.shot.feature a{display:inline-block;margin-top:14px;font-style:italic;font-size:13px}

/* blog */
.mist{left:0;top:2880px;width:1200px;height:378px;background:linear-gradient(180deg,#fff 0%,#f0f0f0 45%,#e2e2e2 100%)}
.blog{left:112px;top:2693px;width:978px;display:grid;grid-template-columns:1fr 1fr;gap:14px 42px}
.post{display:flex;height:235px;background:var(--white);border:1px solid var(--card-line)}
.post-photo{width:211px;flex:none}
.post-body{padding:30px 22px 0}
.post-body h3{font-weight:400;font-size:17px;color:var(--ink);margin-bottom:14px}
.post-body p{font-size:13.5px;line-height:26px;color:var(--muted);font-weight:300}
.post-body a{display:block;margin-top:12px;font-size:13px;font-style:italic;font-weight:300;color:var(--muted)}

/* footer */
.footer{left:0;top:3258px;width:1200px;height:299px;background:var(--footer);color:var(--white)}
.footer .brand{left:110px;top:53px;font-size:29px}
.footer .nav{top:65px;right:114px;font-size:15px}
.footer-rule{left:110px;top:107px;width:980px;height:1px;background:var(--rule)}
.contact{top:150px;display:flex;gap:12px;font-size:15px}
.contact svg{flex:none;margin-top:2px}
.contact strong{display:block;font-weight:400;font-size:16px;margin-bottom:5px}
.contact-split{left:921px;top:140px;width:1px;height:60px;background:var(--rule)}
.social{left:1004px;top:153px;width:38px;height:38px;border-radius:50%;background:var(--white)}
.copyright{left:0;top:260px;width:1200px;text-align:center;font-size:14px;font-weight:300}
</style>
</head>
<body>

<header class="abs hero" role="img" aria-label="Stormy pink and violet sky with a rainbow over green fields and a winding country road">
</header>
<div class="abs brand">CORWIN ASHDALE</div>
<nav class="abs nav"><span>Home</span><span>About</span><span>Gallery</span><span>Contact</span></nav>
<h1 class="abs heading hero-title">AWARD WINNING PHOTOGRAPHER</h1>

<div class="abs welcome-photo" role="img" aria-label="Lone tree on red lichen rocks under a crimson sunset sky"></div>
<section class="abs welcome-text">
  <h2 class="heading">WELCOME</h2>
  <p>Lorem ipsum dolor sit amet, consectetur adipiscing elit, sed do eiusmod tempor incididunt ut labore et dolorgna aliqua. Quis ipsum suspendisse ultrices gravida. Risus commodo viverra maecenas accumsan lacus.</p>
  <p>Sed ut perspiciatis unde omnis iste natus error sit voluptatem accusan tium doloremque laudantium, totam rem aperiam, eaque ipsa quae ab illo inventore veritatis et quasi architecto beatae vitae dicta sunt expli cabo. Nemo enim ipsam voluptatem quia voluptas sit aspernatur.</p>
  <div class="signature">Corwin Ashdale</div>
</section>

<h2 class="heading section-title" style="top:1058px">COLLECTIONS</h2>
<div class="abs collections">
  <div class="tile" role="img" aria-label="Forest creek in the Yarra Valley" style="background:linear-gradient(180deg,#8fa6b8,#4e6a44 55%,#2e3a2a)"><span>YARRA VALLEY &amp; RANGES</span></div>
  <div class="tile" role="img" aria-label="Lone tree on a Tasmanian headland at golden sunset" style="background:linear-gradient(180deg,#f0a83a,#b37a2a 45%,#4a4a1e)"><span>EAST COAST TASMANIA</span></div>
  <div class="tile" role="img" aria-label="Orange sunset over a dark shoreline" style="background:linear-gradient(180deg,#3a4a78,#e07a2a 50%,#2a2622)"><span>LANDSCAPES</span></div>
  <div class="tile" role="img" aria-label="Calm sea under a peach dusk sky" style="background:linear-gradient(180deg,#c8a080,#d89a6a 50%,#8a6a58)"><span>SEASCAPES</span></div>
  <div class="tile" role="img" aria-label="Abandoned vintage car among branches" style="background:linear-gradient(180deg,#5a5a3a,#8a7a4a 55%,#3a3a26)"><span>URBAN</span></div>
  <div class="tile" role="img" aria-label="Snow-capped Himalayan peak above a village at dusk" style="background:linear-gradient(180deg,#0a1a8a,#3a4aa0 45%,#1a1a2a)"><span>NEPAL</span></div>
  <div class="tile" role="img" aria-label="Orange fungus on tree bark" style="background:radial-gradient(circle at 50% 40%,#d8501e,#7a4a2a 55%,#4a3a30)"><span>MACRO</span></div>
</div>

<h2 class="heading section-title" style="top:1589px">GALLERY</h2>
<div class="abs gallery">
  <div class="shot" role="img" aria-label="Lighthouse on a green headland under blue storm clouds" style="background:linear-gradient(180deg,#3a4a80,#6a7aa0 40%,#4a6a30 70%,#2a3a20)"></div>
  <div class="shot feature" role="img" aria-label="Misty valley at dusk near Healesville">
    <h3>Healesville, Yarra Valley</h3>
    <p>Lorem ipsum dolor sit amet, consectetur adip-iscing elit, sed do eiusmod tempor incididunt ut labore et dolore magna aliqua. Quis ipsum suspendisse ultrices gravida. Risus commodo viverra maecenas accumsan lacus vel facilisis.</p>
    <a>Read More</a>
  </div>
  <div class="shot" role="img" aria-label="Silhouettes on a tram bridge against a golden wall" style="background:linear-gradient(90deg,#3a3a3a 40%,#e8d08a 60%,#d8b870)"></div>
  <div class="shot" role="img" aria-label="City towers glowing pink behind trees at dusk" style="background:linear-gradient(180deg,#6a3a7a,#e0608a 35%,#5a2a3a 60%,#2a3a1e)"></div>
  <div class="shot" role="img" aria-label="Rows of old pier pylons in still water at sunset" style="background:linear-gradient(180deg,#6a6aa0,#d89aa0 30%,#3a4a58 55%,#2a3a44)"></div>
  <div class="shot" role="img" aria-label="Country lane beside vineyards under golden light" style="background:linear-gradient(180deg,#3a4a78,#c8a070 40%,#8a7a2a 65%,#5a4a20)"></div>
  <div class="shot" role="img" aria-label="Waterfall over mossy rocks" style="background:linear-gradient(180deg,#3a4a3a,#a0b0b8 40%,#3a4a3a 70%,#2a2a22)"></div>
  <div class="shot" role="img" aria-label="Homestead in a misty rolling valley" style="background:linear-gradient(180deg,#6a5a50,#b09080 40%,#6a7a4a 75%,#3a4a2a)"></div>
  <div class="shot" role="img" aria-label="Black and white Himalayan mountain range" style="background:linear-gradient(180deg,#2a2a2a,#9a9a9a 45%,#4a4a4a 80%,#1a1a1a)"></div>
</div>

<div class="abs mist" role="img" aria-label="Faint misty mountain range backdrop"></div>
<h2 class="heading section-title" style="top:2596px">PHOTOGRAPHY BLOG</h2>
<div class="abs blog">
  <article class="post">
    <div class="post-photo" role="img" aria-label="Three people on a bench at a grey seaside lookout" style="background:linear-gradient(180deg,#4a4a4a,#aaa 50%,#555)"></div>
    <div class="post-body"><h3>Ut enim ad minima veniam.</h3><p>Lorem ipsum dolor sitconsectetur adipiscing elit, sed do eius tempor incididunt ut labore et dolore magna aliqua.</p><a>Read More</a></div>
  </article>
  <article class="post">
    <div class="post-photo" role="img" aria-label="Dead tree silhouette against an orange sunset" style="background:linear-gradient(180deg,#c87a2a,#e8a050 50%,#3a2a1a)"></div>
    <div class="post-body"><h3>Ut enim ad minima veniam.</h3><p>Lorem ipsum dolor sitconsectetur adipiscing elit, sed do eius tempor incididunt ut labore et dolore magna aliqua.</p><a>Read More</a></div>
  </article>
  <article class="post">
    <div class="post-photo" role="img" aria-label="Framed prints hanging on a white wall" style="background:linear-gradient(180deg,#f2f2f2,#e4e4e4 70%,#cfcfcf)"></div>
    <div class="post-body"><h3>Ut enim ad minima veniam.</h3><p>Lorem ipsum dolor sitconsectetur adipiscing elit, sed do eius tempor incididunt ut labore et dolore magna aliqua.</p><a>Read More</a></div>
  </article>
  <article class="post">
    <div class="post-photo" role="img" aria-label="Storm light over a rocky cove" style="background:linear-gradient(180deg,#3a4a6a,#c8907a 40%,#3a3a30 70%,#1e1e1e)"></div>
    <div class="post-body"><h3>Ut enim ad minima veniam.</h3><p>Lorem ipsum dolor sitconsectetur adipiscing elit, sed do eius tempor incididunt ut labore et dolore magna aliqua.</p><a>Read More</a></div>
  </article>
</div>

<footer class="abs footer">
  <div class="abs brand">CORWIN ASHDALE</div>
  <nav class="abs nav"><span>Home</span><span>About</span><span>Gallery</span><span>Contact</span></nav>
  <div class="abs footer-rule"></div>
  <div class="abs contact" style="left:110px">
    <svg width="20" height="24" viewBox="0 0 20 24" fill="none" stroke="#fff" stroke-width="1.5"><path d="M10 23s8-7.5 8-13a8 8 0 0 0-16 0c0 5.5 8 13 8 13z"/><circle cx="10" cy="10" r="3"/></svg>
    <div><strong>ADDRESS</strong>Address comes here</div>
  </div>
  <div class="abs contact" style="left:375px">
    <svg width="24" height="18" viewBox="0 0 24 18" fill="none" stroke="#fff" stroke-width="1.5"><rect x="1" y="1" width="22" height="16"/><path d="M1 1l11 9 11-9"/></svg>
    <div><strong>EMAIL</strong>info@corwinashdale.example</div>
  </div>
  <div class="abs contact" style="left:708px">
    <svg width="22" height="22" viewBox="0 0 24 24" fill="none" stroke="#fff" stroke-width="1.5"><path d="M5 2l4 1 1.5 5-2.5 2a12 12 0 0 0 6 6l2-2.5 5 1.5 1 4c-1 2-3 3-5 3C9 21 3 15 2 7c0-2 1-4 3-5z"/></svg>
    <div><strong>PHONE</strong>+1888-555-0142</div>
  </div>
  <div class="abs contact-split"></div>
  <div class="abs social" aria-label="Social profile"></div>
  <div class="abs copyright">2023 Corwin Ashdale. All Rights Reserved.</div>
</footer>

</body>
</html>
```